Business Card for Brenwick Painting

We need a simple, yet out standing business card for our painting company.

Target Market(s)

wealthy; high-end neighborhoods, and businesses

Industry/Entity Type

Painting

Contact Information for Business Card

Name:
Dorian Vask

Email:
d.vask@brenwick-painting.example

Website:
Brenwick-painting.example

Phone Number:
(555) 412-9063

Font styles to use
Serif
Sans Serif

Requirements
Must have
• slogan "making change simple"
Should not have
• A title attached to the name on the card

```html
<!DOCTYPE html>
<html lang="en">
<head>
<meta charset="utf-8">
<title>Brenwick Painting – Business Card</title>
<link href="https://fonts.googleapis.com/css2?family=Arimo:wght@400;700&display=swap" rel="stylesheet">
<style>
  :root {
    --forest: #3f6410;
    --lime: #b5d335;
    --lime-text: #c3e046;
    --paper: #ffffff;
    --ink-light: #f3f6ea;
    --backdrop: #ecebe6;
  }
  * { margin: 0; padding: 0; box-sizing: border-box; }
  html, body {
    width: 1200px; height: 950px; overflow: hidden;
    background: var(--backdrop);
    font-family: "Arimo", Arial, sans-serif;
  }
  .card {
    position: absolute;
    width: 640px; height: 366px;
    overflow: hidden;
    box-shadow: 0 10px 28px rgba(0,0,0,0.18);
  }
  /* Back of card */
  .card-back {
    left: 110px; top: 70px;
    background: var(--forest);
    color: var(--paper);
  }
  .card-back .wordmark {
    position: absolute; left: 0; right: 0; top: 140px;
    text-align: center;
    font-size: 40px; font-weight: 700; letter-spacing: 2px;
    color: var(--paper);
  }
  .card-back .web {
    position: absolute; left: 0; right: 0; top: 250px;
    text-align: center;
    font-size: 14px; letter-spacing: 4px;
    color: var(--ink-light);
  }
  /* Front of card */
  .card-front {
    left: 450px; top: 510px;
    background: var(--paper);
  }
  .card-front .shapes { position: absolute; inset: 0; }
  .card-front .brand {
    position: absolute; left: 34px; top: 150px;
  }
  .card-front .wordmark {
    font-size: 26px; font-weight: 700; letter-spacing: 0.5px;
    color: var(--forest); white-space: nowrap;
  }
  .card-front .wordmark .dot {
    display: inline-block; width: 15px; height: 15px;
    background: var(--lime); margin-right: 9px; vertical-align: 1px;
  }
  .card-front .slogan {
    margin-top: 8px; margin-left: 24px;
    font-size: 12px; letter-spacing: 3px; text-transform: uppercase;
    color: var(--lime);
    font-weight: 700;
  }
  .contact {
    position: absolute; right: 20px; top: 24px;
    text-align: right; color: var(--paper);
    font-size: 12px; line-height: 1.5;
  }
  .contact .name { color: var(--lime-text); font-size: 17px; font-weight: 700; line-height: 1.2; margin-bottom: 36px; }
  .contact .address { margin-bottom: 18px; }
  .contact .row { display: flex; justify-content: flex-end; align-items: center; gap: 8px; height: 21px; white-space: nowrap; }
  .contact .row svg { width: 13px; height: 13px; flex: none; }
</style>
</head>
<body>

<section class="card card-back" aria-label="Business card back">
  <div class="wordmark">Brenwick Painting</div>
  <div class="web">Brenwick-painting.example</div>
</section>

<section class="card card-front" aria-label="Business card front">
  <svg class="shapes" viewBox="0 0 640 366" preserveAspectRatio="none" aria-hidden="true">
    <rect width="640" height="366" fill="var(--forest)"/>
    <path d="M0 0 H270 C400 40 420 240 350 366 H0 Z" fill="var(--lime)"/>
    <path d="M0 0 H220 C350 40 380 220 320 366 H0 Z" fill="var(--paper)"/>
    <path d="M228 0 C358 40 388 220 328 366" fill="none" stroke="var(--paper)" stroke-width="3"/>
  </svg>

  <div class="brand">
    <div class="wordmark"><span class="dot"></span>Brenwick Painting</div>
    <div class="slogan">making change simple</div>
  </div>

  <div class="contact">
    <div class="name">Dorian Vask</div>
    <div class="address">8350 Larkmoor<br>Drive, Glen Hollow<br>NY 10999</div>
    <div class="row">(555) 412-9063
      <svg viewBox="0 0 16 16"><path d="M3 2h3l1.5 3.5-2 1.3a8 8 0 0 0 3.7 3.7l1.3-2L14 10v3a1 1 0 0 1-1 1A11 11 0 0 1 2 3a1 1 0 0 1 1-1z" fill="var(--lime)"/></svg>
    </div>
    <div class="row">(555) 018-2744
      <svg viewBox="0 0 16 16"><rect x="4" y="1" width="8" height="14" rx="1.5" fill="var(--lime)"/><rect x="5.5" y="3" width="5" height="8" fill="var(--forest)"/></svg>
    </div>
    <div class="row">(555) 019-3381
      <svg viewBox="0 0 16 16"><rect x="2" y="5" width="12" height="9" rx="1" fill="var(--lime)"/><rect x="4" y="1" width="8" height="5" fill="var(--lime)"/><rect x="4" y="9" width="8" height="3" fill="var(--forest)"/></svg>
    </div>
    <div class="row">d.vask@brenwick-painting.example
      <svg viewBox="0 0 16 16"><rect x="1" y="3" width="14" height="10" rx="1" fill="var(--lime)"/><path d="M1.5 4 8 9l6.5-5" fill="none" stroke="var(--forest)" stroke-width="1.3"/></svg>
    </div>
    <div class="row">Brenwick-painting.example
      <svg viewBox="0 0 16 16"><circle cx="8" cy="8" r="7" fill="var(--lime)"/><path d="M1 8h14M8 1c-3 4-3 10 0 14M8 1c3 4 3 10 0 14" fill="none" stroke="var(--forest)" stroke-width="1"/></svg>
    </div>
  </div>
</section>

</body>
</html>
```